Stationery/Logo design for law office

Hello, I am looking for a logo and stationery design for my law office. I am a solo practitioner in New York. I would like the logo to be based around my initials: KRW. Original, I know!
Hello:

I need (1) the logo, (2) a letterhead/stationery design, and (3) an envelope design. I would like the logo to be BLUE. Other than that, I am open and looking forward to seeing different designs.

For my privacy, I am using a sample name/information (the real info will be provided to the winning designer). I would like the logo to consist of the KRW design and the words "Marcus R. Welton Law Office." I plan to use a version with both of those elements, as well as just the KRW design alone.

The information that should go in the letterhead and envelope design is the following:

Marcus R. Welton Law Office
742 Alder Lane
Suite 210
New York, New York 10016
212-384-7265
www.weltonlegalfirm.example

I am open to different formats (changing the order of my contact info, writing the phone number without dashes, etc.); I know it's not a ton of content but I would like it to look good -- and I'm open to both classic and more modern looks.

Note that the sample colors I selected are not meant to be exclusive -- there aren't a ton of options.

Thanks in advance!

• I am leaning toward a design just based on my initials, but I am open to ideas -- just nothing trite like scales of justice or a gavel.

```html
<!DOCTYPE html>
<html lang="en">
<head>
<meta charset="utf-8">
<title>Marcus R. Welton Law Office — Stationery</title>
<link rel="stylesheet" href="https://fonts.googleapis.com/css2?family=Open+Sans:wght@400;600;700&display=swap">
<style>
  :root {
    --brand-blue: #2f7fc2;
    --band-blue: #3d7ab8;
    --card-blue-start: #0a9bd9;
    --card-blue-end: #3676b6;
    --text-grey: #5f5f5f;
    --name-grey: #666666;
    --paper: #ffffff;
    --edge: #cfcfcf;
    --ghost: #f2f2f2;
  }
  html, body {
    margin: 0;
    padding: 0;
    overflow: hidden;
    background: var(--paper);
  }
  .canvas {
    position: relative;
    width: 1080px;
    height: 1200px;
    overflow: hidden;
    background: var(--paper);
    font-family: "Open Sans", Arial, sans-serif;
    color: var(--text-grey);
  }
  .sheet {
    position: absolute;
    overflow: hidden;
    background: var(--paper);
    box-sizing: border-box;
  }
  .wordmark {
    position: absolute;
    font-weight: 700;
    color: var(--brand-blue);
    letter-spacing: 0.02em;
    line-height: 1;
    white-space: nowrap;
  }
  .ghost-mark {
    position: absolute;
    font-weight: 700;
    color: var(--ghost);
    line-height: 1;
    white-space: nowrap;
    letter-spacing: 0.02em;
  }
  .firm-name {
    position: absolute;
    margin: 0;
    font-weight: 600;
    white-space: nowrap;
    color: var(--name-grey);
  }
  .address {
    position: absolute;
    margin: 0;
    font-style: normal;
    font-weight: 400;
    white-space: nowrap;
  }
  .blue-band {
    position: absolute;
    left: 0;
    right: 0;
    bottom: 0;
    background: var(--band-blue);
  }

  /* Letterhead */
  .letterhead {
    left: 0; top: 0; width: 849px; height: 1200px;
    border-right: 1px solid var(--edge);
    border-top: 1px solid var(--edge);
    border-left: 1px solid var(--edge);
  }
  .letterhead .wordmark { left: 92px; top: 88px; font-size: 56px; }
  .letterhead .firm-name { left: 44px; top: 176px; font-size: 17.5px; }
  .letterhead .address { left: 628px; top: 102px; font-size: 14.5px; line-height: 19.4px; }
  .letterhead .ghost-mark { left: 535px; top: 990px; font-size: 122px; }
  .letterhead .blue-band { height: 13px; }

  /* Envelope */
  .envelope {
    left: 232px; top: 261px; width: 848px; height: 329px;
    border: 1px solid #e2e2e2;
    border-bottom: none;
  }
  .envelope .wordmark { left: 78px; top: 50px; font-size: 28px; }
  .envelope .firm-name { left: 43px; top: 95px; font-size: 10px; font-weight: 700; }
  .envelope .address { left: 43px; top: 229px; font-size: 11.2px; line-height: 15.4px; }
  .envelope .ghost-mark { left: 640px; top: 178px; font-size: 78px; }
  .envelope .blue-band { height: 7px; }

  /* Business cards */
  .card {
    top: 618px; width: 333px; height: 205px;
    border-radius: 10px;
  }
  .card-front {
    left: 238px;
    border: 1px solid #e3e3e3;
  }
  .card-front .wordmark { left: 74px; top: 26px; font-size: 26px; }
  .card-front .firm-name { left: 35px; top: 76px; font-size: 10px; font-weight: 700; }
  .card-front .address { left: 35px; top: 112px; font-size: 11.2px; line-height: 15.7px; }
  .card-front .ghost-mark { left: 210px; top: 100px; font-size: 46px; }
  .card-back {
    left: 583px;
    background: linear-gradient(40deg, var(--card-blue-start) 0%, var(--card-blue-end) 100%);
  }
  .card-back .wordmark {
    left: 0; right: 0; top: 60px;
    text-align: center; font-size: 34px; color: var(--paper);
  }
  .card-back .firm-name {
    left: 0; right: 0; top: 131px;
    text-align: center; font-size: 13px; font-weight: 700; color: var(--paper);
  }
</style>
</head>
<body>
<main class="canvas">

  <section class="sheet letterhead" aria-label="Letterhead">
    <span class="ghost-mark" aria-hidden="true">KRW</span>
    <span class="wordmark">KRW</span>
    <h1 class="firm-name">Marcus R. Welton Law Office</h1>
    <address class="address">
      742 Alder Lane<br>
      Suite 210<br>
      New York, New York 10016<br>
      2123847265<br>
      www.weltonlegalfirm.example
    </address>
    <div class="blue-band"></div>
  </section>

  <section class="sheet envelope" aria-label="Envelope">
    <span class="ghost-mark" aria-hidden="true">KRW</span>
    <span class="wordmark">KRW</span>
    <h2 class="firm-name">Marcus R. Welton Law Office</h2>
    <address class="address">
      742 Alder Lane<br>
      Suite 210<br>
      New York, New York 10016<br>
      2123847265<br>
      www.weltonlegalfirm.example
    </address>
    <div class="blue-band"></div>
  </section>

  <section class="sheet card card-front" aria-label="Business card front">
    <span class="ghost-mark" aria-hidden="true">KRW</span>
    <span class="wordmark">KRW</span>
    <h2 class="firm-name">Marcus R. Welton Law Office</h2>
    <address class="address">
      742 Alder Lane<br>
      Suite 210<br>
      New York, New York 10016<br>
      2123847265<br>
      www.weltonlegalfirm.example
    </address>
  </section>

  <section class="sheet card card-back" aria-label="Business card back">
    <span class="wordmark">KRW</span>
    <h2 class="firm-name">Marcus R. Welton Law Office</h2>
  </section>

</main>
</body>
</html>
```